Northern Terrain Published Photographer Website

I need a website to feature a home page slide show of 6 of my top photos then a few simple pages including; gallery, bio, social, checkout, services
Updates

Need extra days to review

Target Market(s)

photography

Industry/Entity Type

Photographer

Coding

Coded - Design and coding required

Number of Pages Required

5+ page

Colors

Designer to choose colors to be used in the design.

Requirements
Must have
• clean eye catching elegant trendy
Nice to have
• unique and creative from other photographer websites

```html
<!DOCTYPE html>
<html lang="en">
<head>
<meta charset="utf-8">
<title>Maren Holloway Photography</title>
<link href="https://fonts.googleapis.com/css2?family=Roboto:wght@300;400;500;700;900&display=swap" rel="stylesheet">
<style>
:root{
  --ink:#000;
  --paper:#fff;
  --purple:#7b3fa0;
  --purple-deep:#5a2d82;
  --text-grey:#555;
  --dusk-1:#2b2a2a;
  --dusk-2:#6b3a1c;
  --dusk-3:#b8621f;
  --teal:#6fb7ae;
  --sand:#e59a3a;
}
*{margin:0;padding:0;box-sizing:border-box}
html,body{width:1200px;height:3260px;overflow:hidden;background:var(--paper);font-family:"Roboto",sans-serif;color:var(--ink)}
.page{position:relative;width:1200px;height:3260px}
.abs{position:absolute}

.site-header{position:absolute;left:0;top:0;width:1200px;height:60px;background:var(--ink);display:flex;align-items:center;justify-content:space-between;padding:0 89px}
.brand{color:var(--paper);font-size:17px;font-weight:400;letter-spacing:.5px;display:flex;align-items:center;gap:8px}
.brand-dot{width:10px;height:10px;border-radius:50%;background:var(--paper)}
.main-nav{display:flex;gap:32px}
.main-nav a{color:var(--paper);text-decoration:none;font-size:13px;font-weight:400;letter-spacing:.2px}

.hero-title{left:89px;top:318px}
.hero-title .first{font-size:84px;font-weight:900;line-height:1;letter-spacing:-1px}
.hero-title .last{font-size:40px;font-weight:700;color:var(--purple);line-height:1;margin-top:0}
.hero-title .role{font-size:18px;font-weight:400;margin-top:4px}

.photo{position:absolute}
.dusk{background:linear-gradient(180deg,var(--dusk-1) 0%,#3a2a22 45%,var(--dusk-2) 75%,#2a1a12 100%)}
.dusk-rock{background:linear-gradient(180deg,#2a2a2c 0%,#5a3a24 40%,var(--dusk-3) 60%,#3a2012 100%)}
.lake{background:linear-gradient(180deg,var(--teal) 0%,#d9a255 40%,var(--sand) 60%,#7fb9ae 100%)}
.lake-rock{background:linear-gradient(180deg,#e7a14a 0%,#f0b55a 55%,#c8842f 75%,#d69a48 100%)}

.intro{left:613px;top:852px;width:490px}
.section-heading{font-size:38px;font-weight:700;line-height:1;letter-spacing:-.3px}
.intro p{margin-top:14px;font-size:16px;line-height:26px;font-weight:300;color:var(--text-grey)}

.services-title{left:0;top:1278px;width:1200px;text-align:center}
.service{position:absolute;top:1365px;width:330px;height:100px}
.service svg{position:absolute;left:0;top:0}
.service h3{position:absolute;left:104px;top:0;font-size:20px;font-weight:400;line-height:20px;text-transform:uppercase}
.service p{position:absolute;left:104px;top:52px;font-size:14.5px;line-height:22px;font-weight:300;color:var(--text-grey);width:210px}

.gallery{position:absolute;left:0;top:1541px;width:1200px;height:652px;display:grid;grid-template-columns:400px 400px 400px;grid-template-rows:326px 326px}
.g1{background:linear-gradient(180deg,#6d9ed6 0%,#cfdcea 35%,#3f5a3a 55%,#8aa0b8 100%)}
.g2{background:linear-gradient(180deg,#86b4e2 0%,#b05a3c 40%,#a88a6a 70%,#6a5040 100%)}
.g3{background:linear-gradient(180deg,#8a8a8e 0%,#c9c4bb 35%,#4d8c94 60%,#c49a6c 100%);position:relative}
.g4{background:linear-gradient(180deg,#3a1a22 0%,#d9482a 35%,#f0853a 55%,#1d2420 75%,#d8d8dc 100%)}
.g5{background:linear-gradient(180deg,#6ec2b5 0%,#e2a046 45%,#f3b45c 60%,#a77a3a 100%)}
.g6{background:linear-gradient(135deg,#b34a20 0%,#6b86ad 40%,#c6c9d4 55%,#a5582e 80%,#6b3a22 100%)}
.g3 svg{position:absolute;left:158px;top:147px}

.banner{position:absolute;left:0;top:2193px;width:1200px;height:478px;background:radial-gradient(circle at 600px 260px,#b89ae0 0%,#7d5bc0 28%,#5d3f9a 55%,#3d2a6a 100%)}
.banner-text{position:absolute;left:0;top:2395px;width:1200px;text-align:center;color:var(--paper)}
.banner-text .big{font-size:78px;font-weight:700;line-height:1;letter-spacing:-1px}
.banner-text .small{font-size:34px;font-weight:400;line-height:1;margin-top:2px}

.newsletter{position:absolute;left:0;top:2671px;width:1200px;height:183px;background:var(--purple)}
.newsletter h2{position:absolute;left:89px;top:70px;color:var(--paper);font-size:36px;font-weight:500;line-height:1}
.newsletter p{position:absolute;left:89px;top:107px;color:var(--paper);font-size:14px;font-weight:300}
.signup{position:absolute;left:682px;top:77px;display:flex;height:48px}
.signup .field{width:294px;background:var(--paper);font-size:14px;color:#555;padding:17px 22px 0}
.signup .button{width:135px;background:var(--ink);color:var(--paper);font-size:14px;font-weight:700;text-align:center;line-height:48px}

.site-footer{position:absolute;left:0;top:2854px;width:1200px;height:406px;background:var(--ink);color:var(--paper)}
.copyright{position:absolute;left:89px;top:166px;font-size:17px;line-height:22px;font-weight:400}
.footer-brand{position:absolute;left:0;top:178px;width:1200px;text-align:center;font-size:34px;font-weight:300;letter-spacing:1px}
.footer-brand small{display:block;font-size:12px;letter-spacing:3px;margin-top:4px}
.social{position:absolute;top:172px;width:66px;height:66px;border-radius:50%;display:flex;align-items:center;justify-content:center;font-size:11px;font-weight:500;color:var(--paper)}
.social.active{background:var(--purple)}
.to-top{position:absolute;left:580px;top:331px;width:40px;height:40px;border-radius:50%;background:var(--purple)}
.to-top svg{position:absolute;left:14px;top:15px}
</style>
</head>
<body>
<div class="page">

  <header class="site-header">
    <div class="brand"><span>Maren Holloway</span><span class="brand-dot"></span></div>
    <nav class="main-nav">
      <a href="#">GALLERY</a><a href="#">BIO</a><a href="#">SOCIAL</a><a href="#">CHECKOUT</a><a href="#">SERVICES</a>
    </nav>
  </header>

  <div class="abs hero-title">
    <div class="first">MAREN</div>
    <div class="last">HOLLOWAY</div>
    <div class="role">PHOTOGRAPHY</div>
  </div>

  <div class="photo dusk" style="left:613px;top:204px;width:129px;height:154px" role="img" aria-label="Storm clouds over desert at dusk"></div>
  <div class="photo dusk-rock" style="left:756px;top:127px;width:206px;height:404px" role="img" aria-label="Sunlit butte at dusk"></div>
  <div class="photo dusk" style="left:976px;top:233px;width:135px;height:163px" role="img" aria-label="Dark sky over mesa"></div>
  <div class="photo dusk" style="left:552px;top:376px;width:190px;height:257px" role="img" aria-label="Desert slope in evening light"></div>
  <div class="photo dusk" style="left:976px;top:413px;width:129px;height:154px" role="img" aria-label="Canyon floor at sunset"></div>
  <div class="photo dusk" style="left:757px;top:546px;width:135px;height:162px" role="img" aria-label="Shadowed desert sand"></div>

  <div class="photo lake" style="left:139px;top:775px;width:106px;height:130px" role="img" aria-label="Rock edge against teal sky"></div>
  <div class="photo lake-rock" style="left:257px;top:710px;width:171px;height:338px" role="img" aria-label="Golden sandstone rock reflected in lake"></div>
  <div class="photo lake" style="left:439px;top:800px;width:113px;height:135px" role="img" aria-label="Distant cliffs by the lake"></div>
  <div class="photo lake" style="left:89px;top:920px;width:157px;height:215px" role="img" aria-label="Lake reflection of rock"></div>
  <div class="photo lake" style="left:439px;top:951px;width:108px;height:129px" role="img" aria-label="Cliff reflection in water"></div>
  <div class="photo lake-rock" style="left:258px;top:1061px;width:113px;height:137px" role="img" aria-label="Rippled golden reflection"></div>

  <section class="abs intro">
    <h2 class="section-heading">SHORT<br>INTRODUCTION</h2>
    <p>Lorem Ipsum is simply dummy text of the printing and typesetting industry. Lorem Ipsum has been the industry's standard dummy text ever since the 1500s, when an unknown printer took a galley of type and scrambled it to make a type specimen book.</p>
  </section>

  <h2 class="abs section-heading services-title">SERVICES OVERVIEW</h2>

  <div class="service" style="left:89px">
    <svg width="79" height="72" viewBox="0 0 79 72" fill="none" stroke="#7b3fa0" stroke-width="2.5">
      <path d="M1 14V1h13M65 1h13v13M78 58v13H65M14 71H1V58"/>
      <circle cx="39.5" cy="40" r="16"/><path d="M23.5 40h32M39.5 24c-8 10-8 22 0 32M39.5 24c8 10 8 22 0 32"/>
      <path d="M39.5 30c-5 0-8-3.5-8-7.5s3.5-7.5 8-7.5 8 3.5 8 7.5-3 7.5-8 7.5z" fill="#7b3fa0"/>
    </svg>
    <h3>Geographic<br>Photographer</h3>
    <p>Lorem Ipsum is simply dummy text of the and typesetting .</p>
  </div>
  <div class="service" style="left:448px">
    <svg width="79" height="72" viewBox="0 0 79 72" fill="none" stroke="#7b3fa0" stroke-width="2.5">
      <path d="M1 14V1h13M65 1h13v13M78 58v13H65M14 71H1V58"/>
      <rect x="22" y="22" width="36" height="28" fill="#7b3fa0"/>
      <path d="M26 46l9-12 7 8 5-5 8 9z" fill="#fff" stroke="none"/><circle cx="50" cy="29" r="3" fill="#fff" stroke="none"/>
    </svg>
    <h3>Nature<br>Photography</h3>
    <p>Lorem Ipsum is simply dummy text of the and typesetting .</p>
  </div>
  <div class="service" style="left:810px">
    <svg width="79" height="72" viewBox="0 0 79 72" fill="none" stroke="#7b3fa0" stroke-width="2.5">
      <path d="M1 14V1h13M65 1h13v13M78 58v13H65M14 71H1V58"/>
      <rect x="20" y="24" width="39" height="28" rx="5" fill="#7b3fa0"/>
      <circle cx="39.5" cy="38" r="8" fill="#fff" stroke="none"/><rect x="33" y="19" width="13" height="6" fill="#7b3fa0"/>
    </svg>
    <h3>Family<br>Photography</h3>
    <p>Lorem Ipsum is simply dummy text of the and typesetting .</p>
  </div>

  <div class="gallery">
    <div class="g1" role="img" aria-label="Snowy river valley reflecting clouds"></div>
    <div class="g2" role="img" aria-label="Wild sheep grazing before red cliffs"></div>
    <div class="g3" role="img" aria-label="Lake among desert cliffs under clouds">
      <svg width="82" height="64" viewBox="0 0 82 64"><path d="M8 14h16l7-10h20l7 10h16a6 6 0 0 1 6 6v36a6 6 0 0 1-6 6H8a6 6 0 0 1-6-6V20a6 6 0 0 1 6-6z" fill="#fff"/><circle cx="41" cy="38" r="15" fill="none" stroke="#333" stroke-width="5"/></svg>
    </div>
    <div class="g4" role="img" aria-label="Fiery sunset over snowy forest"></div>
    <div class="g5" role="img" aria-label="Sandstone rock reflected in calm lake"></div>
    <div class="g6" role="img" aria-label="Glass sphere on canyon arch at sunrise"></div>
  </div>

  <div class="banner" role="img" aria-label="Glass sphere on a frosted shore at twilight"></div>
  <div class="banner-text">
    <div class="big">PHOTOGRAPHER</div>
    <div class="small">WELCOME TO THE GALLERY!</div>
  </div>

  <section class="newsletter">
    <h2>SUBSCRIBE TO MY NEWSLETTER</h2>
    <p>Lorem Ipsum is simply dummy text of the printing and typesetting industry.</p>
    <div class="signup"><div class="field">Email Address</div><div class="button">SUBSCRIBE</div></div>
  </section>

  <footer class="site-footer">
    <div class="copyright">Copyright 2019<br>All Right Reserved</div>
    <div class="footer-brand">Maren Holloway<small>PHOTOGRAPHY</small></div>
    <div class="social" style="left:889px">Friendwall</div>
    <div class="social active" style="left:967px">Chirper</div>
    <div class="social" style="left:1042px">Snapgrid</div>
    <div class="to-top"><svg width="12" height="8" viewBox="0 0 12 8"><path d="M1 7l5-5 5 5" fill="none" stroke="#fff" stroke-width="2"/></svg></div>
  </footer>

</div>
</body>
</html>
```